Campaign Flyer for a local election

Black and white election flyer

See information below to be included:

Re-elect Dorian
Experienced Willows Board Member
Experienced NYC Principal
Experienced leader

One Year Board Accomplishments:
-Installed New Park Lights (Bollards)
-Red Brick Road Repair Project
-Established Closer Ties with Our local precinct to frequently monitor the community with directed security patrols. Requested an increased police presence.
-Met with the 62nd Precinct Officials & Assemblywoman, Marla Quintrell to discuss our security issues
- Focused on maintenance of streetlights to make brighter streets
-Negotiated Contract & Hired Our New Landscaper, Oakhollow Landscapers
-Major Homeowner Shrub Replacement Project
- Addressing Standing Water in our Park (Installed French Drain)
- Replaced and upgraded all 5 outdoor circuit breaker panels
-Write monthly community newsletters
-Sewer cleaning project (had all community catch basins cleaned)
-Carefully overseeing our new school project. Coordinating with the sponsor and the school directors
-Delivered a very healthy budget to the community
-Works closely with our committees
-Events: Zoo event, Petting Zoo, Outdoor Movie Night, Egg Hunt

It is my intent to seek re-election.
(Photo) Dorian Lindqvist
-Dedicated to improving our community
-Hard-working…He gets thing done!
-Trustworthy

. .

Please note, I am submitting new information under accomplishments. The list of accomplishments should be in the same sequence, starting with: Met with the 62nd Precinct....
Please carefully review.
----------------------------------------------------------------------------------------------------------------------------------------------------------------

Re-elect Dorian
Experienced NYC Principal
Experienced leader

Last Year’s Board Accomplishments:

-Met with the 62nd Precinct Officials & Assemblywoman, Marla Quintrell, to discuss our security issues. Requested increased police presence.
-Established a strong partnership with the 62nd precinct to frequently monitor the community with directed security patrols.
-Replaced all new park lights (Bollards) to make the park brighter
- Focused on maintenance of streetlights to make streets brighter
-‘Fixing Our Streets Project’ (Repaired all cracked/missing red bricks)
-Homeowner Shrub Replacement Project (Replaced hundreds of bushes)
- I write the monthly community newsletter
-Carefully overseeing our new school project. Coordinating with the sponsor and the school director
-Monitoring C of O’s and homeowners Insurance

(Photo) Dorian Lindqvist
-Hard-working! I get things done!
-Trustworthy

. .

Re-elect Dorian
Experienced NYC Principal
Experienced leader

(Photo) Dorian Lindqvist
-Trustworthy

. .

Target Market(s)

A Community electing a Board Member

Industry/Entity Type

residential election

Requirements
Must have
• all black, white and grey print. Flyers will not be printed in color
Nice to have
• See the information in the attachment below containing all my accomplishments
Should not have
• color

```html
<!DOCTYPE html>
<html lang="en">
<head>
<meta charset="utf-8">
<title>Re-elect Dorian — Campaign Flyer</title>
<link href="https://fonts.googleapis.com/css2?family=DM+Serif+Display&family=Poppins:wght@500;600;700;800&family=Arimo&display=swap" rel="stylesheet">
<style>
  :root {
    --ink: #333334;
    --white: #ffffff;
    --band-grey: #d3d4d6;
    --photo-light: #7a7a7a;
    --photo-mid: #4a4a4a;
    --photo-dark: #262626;
  }
  html, body {
    margin: 0;
    padding: 0;
    width: 941px;
    height: 1200px;
    overflow: hidden;
    background: var(--white);
  }
  .flyer {
    position: relative;
    width: 941px;
    height: 1200px;
    overflow: hidden;
    background: var(--white);
  }

  /* Hero */
  .hero {
    position: absolute;
    left: 0; top: 0;
    width: 941px; height: 537px;
  }
  .hero-photo {
    position: absolute;
    inset: 0;
    background:
      radial-gradient(ellipse 220px 300px at 200px 330px, rgba(150,150,150,0.35), transparent 70%),
      linear-gradient(175deg, var(--photo-light) 0%, var(--photo-mid) 16%, var(--photo-dark) 60%, #303030 100%);
  }
  .headline {
    position: absolute;
    right: 45px;
    top: 60px;
    margin: 0;
    font-family: "DM Serif Display", serif;
    font-weight: 400;
    color: var(--white);
    text-align: right;
    line-height: 1;
  }
  .headline-lead {
    display: block;
    font-size: 112px;
    letter-spacing: -1px;
    margin-right: 20px;
  }
  .headline-name {
    display: block;
    font-size: 178px;
    letter-spacing: -3px;
    margin-top: -38px;
  }
  .credentials {
    position: absolute;
    left: 356px;
    top: 340px;
    width: 520px;
    margin: 0;
    padding: 0;
    list-style: none;
    font-family: "Poppins", sans-serif;
    font-weight: 700;
    font-size: 26px;
    color: var(--white);
  }
  .credentials li {
    display: flex;
    align-items: center;
    gap: 18px;
    height: 44px;
    padding: 8px 0;
  }
  .credentials li + li {
    border-top: 2px dashed rgba(255,255,255,0.9);
  }
  .credentials li:first-child { padding-top: 0; }
  .tick { flex: none; }

  /* Accomplishments */
  .accomplishments {
    position: absolute;
    left: 0; top: 537px;
    width: 941px; height: 393px;
    background: var(--band-grey);
  }
  .accomplishments h2 {
    position: absolute;
    left: 66px; top: 36px;
    margin: 0;
    font-family: "Poppins", sans-serif;
    font-weight: 600;
    font-size: 30px;
    line-height: 1;
    letter-spacing: -0.5px;
    color: var(--ink);
  }
  .accomplishment-list {
    position: absolute;
    top: 90px;
    margin: 0;
    padding: 0 0 0 14px;
    font-family: "Arimo", Arial, sans-serif;
    font-size: 15.3px;
    line-height: 17px;
    color: var(--ink);
  }
  .accomplishment-list li { margin-bottom: 8px; padding-left: 0; }
  .accomplishment-list li::marker { font-size: 11px; }
  .list-left { left: 67px; width: 380px; }
  .list-right { left: 498px; width: 364px; }

  /* Sign-off */
  .sign-off {
    position: absolute;
    left: 0; top: 930px;
    width: 941px; height: 270px;
    background: var(--white);
    font-family: "Poppins", sans-serif;
    color: var(--ink);
  }
  .intent {
    position: absolute;
    left: 70px; top: 26px;
    margin: 0;
    font-weight: 600;
    font-size: 37px;
    letter-spacing: 0.6px;
  }
  .candidate-name {
    position: absolute;
    left: 74px; top: 72px;
    margin: 0;
    font-weight: 800;
    font-size: 60px;
    letter-spacing: -0.5px;
    line-height: 1.1;
  }
  .qualities {
    position: absolute;
    left: 79px; top: 156px;
    margin: 0; padding: 0;
    list-style: none;
    font-weight: 600;
    font-size: 22px;
  }
  .qualities li {
    display: flex;
    align-items: center;
    gap: 12px;
    height: 31.5px;
  }
</style>
</head>
<body>
<main class="flyer">

  <section class="hero">
    <div class="hero-photo" role="img" aria-label="Black and white photo of candidate Dorian Lindqvist smiling in front of beach dunes with grass and ocean behind"></div>
    <h1 class="headline">
      <span class="headline-lead">Re-elect</span>
      <span class="headline-name">Dorian</span>
    </h1>
    <ul class="credentials">
      <li>
        <svg class="tick" width="18" height="18" viewBox="0 0 18 18" aria-hidden="true"><path d="M13 2H2v14h14V9" fill="none" stroke="#fff" stroke-width="1.6"/><path d="M5 8l4 4 8-10" fill="none" stroke="#fff" stroke-width="1.8"/></svg>
        Experienced Willows Board Member
      </li>
      <li>
        <svg class="tick" width="18" height="18" viewBox="0 0 18 18" aria-hidden="true"><path d="M13 2H2v14h14V9" fill="none" stroke="#fff" stroke-width="1.6"/><path d="M5 8l4 4 8-10" fill="none" stroke="#fff" stroke-width="1.8"/></svg>
        Experienced NYC Principal
      </li>
      <li>
        <svg class="tick" width="18" height="18" viewBox="0 0 18 18" aria-hidden="true"><path d="M13 2H2v14h14V9" fill="none" stroke="#fff" stroke-width="1.6"/><path d="M5 8l4 4 8-10" fill="none" stroke="#fff" stroke-width="1.8"/></svg>
        Experienced leader
      </li>
    </ul>
  </section>

  <section class="accomplishments">
    <h2>ONE YEAR BOARD ACCOMPLISHMENTS:</h2>
    <ul class="accomplishment-list list-left">
      <li>Installed New Park Lights (Bollards)</li>
      <li>Red Brick Road Repair Project</li>
      <li>Established Closer Ties with Our local precinct to frequently monitor the community with directed security patrols. Requested an increased police presence.</li>
      <li>Met with the 62nd Precinct Officials &amp; Assembly woman, Marla Quintrell to discuss our security issues</li>
      <li>Focused on maintenance of streetlights to make brighter streets</li>
      <li>Negotiated Contract &amp; Hired Our New Landscaper, Oakhollow Landscapers</li>
      <li>Major Home owner Shrub Replacement Project</li>
      <li>Addressing Standing Water in our Park (Installed French Drain)</li>
    </ul>
    <ul class="accomplishment-list list-right">
      <li>Replaced and upgraded all 5 outdoor circuit breaker panels</li>
      <li>Write monthly community newsletters</li>
      <li>Sewer cleaning project (had all community catch basins cleaned)</li>
      <li>Carefully overseeing our new school project. Coordinating with the sponsor and the school directors</li>
      <li>Delivered a very healthy budget to the community</li>
      <li>Works closely with our committees</li>
      <li>Events: Zoo event, Petting Zoo, Outdoor Movie Night, Egg Hunt</li>
    </ul>
  </section>

  <section class="sign-off">
    <p class="intent">IT IS MY INTENT TO SEEK RE-ELECTION.</p>
    <h2 class="candidate-name">DORIAN LINDQVIST</h2>
    <ul class="qualities">
      <li>
        <svg class="tick" width="15" height="15" viewBox="0 0 18 18" aria-hidden="true"><path d="M13 2H2v14h14V9" fill="none" stroke="#333334" stroke-width="1.6"/><path d="M5 8l4 4 8-10" fill="none" stroke="#333334" stroke-width="1.8"/></svg>
        Dedicated to improving our community
      </li>
      <li>
        <svg class="tick" width="15" height="15" viewBox="0 0 18 18" aria-hidden="true"><path d="M13 2H2v14h14V9" fill="none" stroke="#333334" stroke-width="1.6"/><path d="M5 8l4 4 8-10" fill="none" stroke="#333334" stroke-width="1.8"/></svg>
        Hard-working…He gets thing done!
      </li>
      <li>
        <svg class="tick" width="15" height="15" viewBox="0 0 18 18" aria-hidden="true"><path d="M13 2H2v14h14V9" fill="none" stroke="#333334" stroke-width="1.6"/><path d="M5 8l4 4 8-10" fill="none" stroke="#333334" stroke-width="1.8"/></svg>
        Trustworthy
      </li>
    </ul>
  </section>

</main>
</body>
</html>
```